Catchy Cards for Hospital

I run a rural hospital in Texas called Pellor Valley Hospital and am in need of contemporary business cards for all of my Department Heads. While our logo is somewhat simplistic, I don't have the option of changing it at this time, so anything to make the rest of the card present the appearance of a modern, professional healthcare facility would be great. Although the attached files are in black, our hospital colors are in a copper brown and black. I need to be able to change the name and title on the card so I can get cards printed for various department heads.

Target Market(s)

Referring physicians, large hospital systems, national organizations, state and federal government

Industry/Entity Type

Hospital

Contact Information for Business Card

Name Dale Hoskin
Title CEO

Phone: Main 555-214-0147 & Direct xxxxxx
Fax xxxxx
dale.hoskin@pellorvh.example
382 Wimble Street Box 415
Marrowby, Calden 76902

Font styles to use
Serif

Colors
f48340

Requirements
Must have
• Clean crisp lines and ability to modify names, titles and emails
• On the back "PellorValleyHospital.Example
Nice to have
• Needs to be in line with logo, which is a bit dated and not too appealing, but I'm hoping that the rest of the card can make up for that fact just a little bit.
• Hospital's colors are a copper brown, black and white
Should not have
• Shapes or anything distracting

```html
<!DOCTYPE html>
<html lang="en">
<head>
<meta charset="utf-8">
<title>Pellor Valley Hospital — Business Card</title>
<link href="https://fonts.googleapis.com/css2?family=Source+Sans+3:wght@400;600&display=swap" rel="stylesheet">
<style>
  :root {
    --backdrop: #000000;
    --copper: #f38540;
    --paper: #ffffff;
    --ink: #111111;
    --on-copper: #ffffff;
  }
  * { margin: 0; padding: 0; box-sizing: border-box; }
  html, body {
    width: 1200px;
    height: 900px;
    overflow: hidden;
    background: var(--backdrop);
    font-family: "Source Sans 3", "Myriad Pro", sans-serif;
  }
  .canvas {
    position: relative;
    width: 1200px;
    height: 900px;
  }
  .card {
    position: absolute;
    top: 200px;
    width: 310px;
    height: 502px;
  }
  .card--front {
    left: 265px;
    background: var(--copper);
    border-radius: 66px 0 66px 0;
    color: var(--on-copper);
    text-align: center;
  }
  .card--back {
    left: 641px;
    background: var(--paper);
    border-radius: 0 66px 0 66px;
  }
  .holder-name {
    position: absolute;
    top: 117px;
    left: 0;
    right: 0;
    font-size: 26px;
    font-weight: 600;
    line-height: 32px;
  }
  .holder-title {
    position: absolute;
    top: 151px;
    left: 0;
    right: 0;
    font-size: 19px;
    font-weight: 400;
    line-height: 24px;
  }
  .rule {
    position: absolute;
    left: 62px;
    width: 186px;
    height: 2px;
    background: var(--on-copper);
  }
  .rule--upper { top: 191px; }
  .rule--lower { top: 342px; }
  .contact-list {
    position: absolute;
    top: 215px;
    left: 0;
    right: 0;
    list-style: none;
    font-size: 19px;
    line-height: 27.7px;
  }
  .contact-list strong { font-weight: 600; }
  .address {
    position: absolute;
    top: 358px;
    left: 0;
    right: 0;
    font-style: normal;
    font-size: 19px;
    line-height: 28px;
  }
  .wordmark {
    position: absolute;
    top: 192px;
    left: 38px;
    right: 24px;
    color: var(--ink);
    font-size: 32px;
    font-weight: 600;
    line-height: 36px;
  }
  .wordmark span { display: block; }
  .wordmark span:nth-child(2) { padding-left: 22px; }
  .wordmark span:nth-child(3) { padding-left: 44px; }
</style>
</head>
<body>
  <main class="canvas">
    <section class="card card--front" aria-label="Card front">
      <h1 class="holder-name">Dale Hoskin</h1>
      <p class="holder-title">CEO</p>
      <div class="rule rule--upper"></div>
      <ul class="contact-list">
        <li><strong>Direct:</strong> 555-214-0147</li>
        <li>Phone: 555-214-0147</li>
        <li>Fax: 555-214-0147</li>
        <li>dale.hoskin@pellorvh.example</li>
      </ul>
      <div class="rule rule--lower"></div>
      <address class="address">
        382 Wimble Street Box 415<br>
        Marrowby, Calden 76902
      </address>
    </section>

    <section class="card card--back" aria-label="Card back">
      <p class="wordmark">
        <span>Pellor</span>
        <span>Valley</span>
        <span>Hospital</span>
      </p>
    </section>
  </main>
</body>
</html>
```